Seller Looking for a luxurious diverse ethnic look...stunning but not overly seductive

I need a web Design for a company based in NEW YORK CITY called Torvane Crest LLC. Initially I will be selling clothing and accessories as well as electronics on Quibra and hope to branch out. I want the whole experience for my customers and people I will buy from when they deal with me to be confident that this will be a torvane crest and luxurious transaction.
Updates

Project Deadline Extended Reason: As I keep getting these great designs I continue to get more ideas and feel more time will help get us there. Added Thursday, July 16, 2015

Target Market(s)

ages 20-60

Industry/Entity Type

Clothing

Number of Pages Required

1 page

Font styles to use
Script

Colors
b768aa

Requirements
Must have
• Sleek and Luxurious feel and modern. I would like the page to look startling stunning yet not overly seductive and to include ethnic diversity. I like the illusion not knowing what the sight is selling since I am not targeting one area.
Should not have
• Do not want it to look generic or traditional

```html
<!DOCTYPE html>
<html lang="en">
<head>
<meta charset="utf-8">
<title>Torvane Crest</title>
<link href="https://fonts.googleapis.com/css2?family=Open+Sans:wght@400;600;700;800&display=swap" rel="stylesheet">
<style>
:root{
  --plum:#b768aa;
  --plum-dark:#9c5190;
  --ink:#333333;
  --muted:#777777;
  --line:#e3e3e3;
  --paper:#ffffff;
  --mist:#f4f4f4;
  --grey-band:#ececec;
  --footer:#2f2f31;
  --footer-base:#232325;
}
*{box-sizing:border-box;margin:0;padding:0}
html,body{width:1200px;height:2548px;overflow:hidden}
body{font-family:"Open Sans",Arial,sans-serif;color:var(--ink);background:var(--paper);position:relative}
.wrap{width:1000px;margin:0 auto;position:relative}

/* top bar */
.topbar{height:30px;border-bottom:1px solid var(--line);font-size:11px;color:var(--muted)}
.topbar .wrap{display:flex;justify-content:space-between;align-items:center;height:30px}
.topbar nav a{margin-right:18px;color:var(--muted);text-decoration:none;text-transform:uppercase}
.cart{color:var(--plum);text-transform:uppercase;display:flex;align-items:center;gap:6px}

/* header */
.header{height:145px}
.header .wrap{display:flex;align-items:center;justify-content:space-between;height:145px}
.logo{font-size:27px;font-weight:800;letter-spacing:1px;color:var(--ink);text-transform:uppercase}
.hotline{display:flex;align-items:center;gap:12px}
.hotline small{display:block;font-size:11px;color:var(--muted);text-transform:uppercase}
.hotline strong{display:block;font-size:24px;color:var(--plum);font-weight:700;letter-spacing:1px}
.search{width:200px;height:30px;border:1px solid var(--line);font-size:11px;color:#aaa;display:flex;align-items:center;justify-content:space-between;padding:0 10px}

/* nav */
.mainnav{background:var(--plum);height:52px}
.mainnav ul{list-style:none;display:flex;justify-content:space-between;height:52px;align-items:center;width:1000px;margin:0 auto}
.mainnav li{color:#fff;font-size:12px;text-transform:uppercase;font-weight:600}

/* hero */
.hero{position:relative;height:392px;background:linear-gradient(90deg,#8a7d86 0%,#b9a9ae 35%,#e6d7cf 65%,#cdb9b4 100%)}
.hero .wrap{height:392px}
.hero-copy{position:absolute;left:0;top:95px;width:440px}
.hero h1{color:#fff;font-size:30px;line-height:38px;font-weight:700;text-transform:uppercase}
.hero p{color:#fff;font-size:11px;line-height:17px;margin:16px 0 20px;opacity:.9}
.btn{display:inline-block;background:var(--plum);color:#fff;font-size:11px;text-transform:uppercase;padding:9px 18px;font-weight:600}
.arrow{position:absolute;top:180px;width:30px;height:30px}
.arrow.left{left:20px}.arrow.right{right:20px}
.hero-strip{height:20px;background:var(--plum)}

/* welcome */
.welcome{height:360px;text-align:center;padding-top:75px}
.welcome h2{color:var(--plum);font-size:22px;font-weight:700;text-transform:uppercase}
.welcome p{font-size:11px;line-height:18px;color:var(--muted);width:940px;margin:20px auto 28px}

/* categories */
.categories{background:var(--grey-band);height:380px;padding-top:32px}
.categories .wrap{display:flex;justify-content:space-between}
.cat{width:312px;height:308px;position:relative;box-shadow:0 4px 10px rgba(0,0,0,.15)}
.cat h3{position:absolute;top:30px;left:0;right:0;text-align:center;color:#fff;font-size:38px;font-weight:800;text-transform:uppercase;line-height:40px}
.cat h3 span{display:block;font-size:22px;font-weight:600;line-height:26px}
.cat .zoom{position:absolute;left:126px;top:136px}
.cat-cloth{background:linear-gradient(135deg,#6c3e4e,#a0566b 50%,#3d5c7a)}
.cat-acc{background:linear-gradient(135deg,#c9b8a6,#8d7b6d 55%,#5b4b44)}
.cat-elec{background:linear-gradient(135deg,#4a4a4f,#8c8c91 55%,#2e2e33)}

/* products */
.featured{height:560px;padding-top:52px}
.featured-head{text-align:center;position:relative;border-bottom:1px solid var(--line);padding-bottom:14px}
.featured-head h2{font-size:20px;font-weight:700;text-transform:uppercase}
.pager{position:absolute;right:0;top:0;display:flex;gap:6px}
.products{display:flex;justify-content:space-between;margin-top:18px}
.product{width:200px;text-align:center}
.product .shot{height:172px}
.product .price{margin-top:16px;font-size:20px;color:var(--plum);font-weight:700}
.product .price s{color:#999;font-size:16px;font-weight:400;margin-left:4px}
.product h4{font-size:12px;text-transform:uppercase;margin-top:6px;font-weight:700}
.product p{font-size:10px;color:var(--muted);line-height:15px;margin-top:8px}
.product .actions{display:flex;justify-content:space-between;margin-top:14px}
.shot-1{background:linear-gradient(135deg,#3b6aa8,#d8cf4a 50%,#c43b3b)}
.shot-2{background:linear-gradient(135deg,#2b2b2b,#c94a4a 45%,#e0b43a 70%,#3a7ec4)}
.shot-3{background:linear-gradient(135deg,#5c3a2e,#c7906a 55%,#2a2a2a)}
.shot-4{background:linear-gradient(135deg,#d8d8d8,#8a8a8a 50%,#3c3c3c)}

/* promo */
.promo{height:325px;position:relative;background:linear-gradient(90deg,#d6a98e 0%,#e6cfc3 35%,#d6b7a8 65%,#c9a2a4 100%);margin-top:2px}
.promo-copy{position:absolute;right:100px;top:92px;text-align:right;color:#fff}
.promo-copy h2{font-size:46px;font-weight:700;text-transform:uppercase;line-height:52px}
.promo-copy p{font-size:22px;margin-top:4px}

/* footer */
.footer{background:var(--footer);height:252px;color:#bbb;font-size:11px;padding-top:28px}
.footer .wrap{display:flex;justify-content:space-between}
.footer h5{color:var(--plum);font-size:11px;text-transform:uppercase;margin-bottom:12px;font-weight:700}
.col-nav{width:140px}.col-nav li{list-style:none;line-height:18px}
.col-news{width:220px}.col-news p{line-height:16px}
.field{width:150px;height:24px;background:#fff;color:#999;font-size:10px;padding:5px 8px;margin:8px 0}
.btn-sm{display:inline-block;background:var(--plum);color:#fff;font-size:10px;text-transform:uppercase;padding:6px 20px}
.col-follow{width:180px}
.socials{display:flex;gap:6px}
.market{margin-top:26px;color:var(--plum);font-size:30px;font-weight:700;display:flex;align-items:center;gap:8px}
.col-contact{width:200px}.col-contact li{list-style:none;line-height:19px;display:flex;gap:8px;align-items:center}
.base{background:var(--footer-base);height:36px;color:#888;font-size:10px}
.base .wrap{display:flex;justify-content:center;align-items:center;height:36px}
.base em{color:var(--plum);font-style:normal;margin-right:4px}
</style>
</head>
<body>

<header>
  <div class="topbar"><div class="wrap">
    <nav><a>Login</a><a>Create an Account</a><a>Wishlist</a></nav>
    <div class="cart">
      <svg width="14" height="12" viewBox="0 0 14 12"><path d="M0 1h3l2 7h7l2-5H4" fill="none" stroke="#b768aa" stroke-width="1.4"/><circle cx="6" cy="10.5" r="1.2" fill="#b768aa"/><circle cx="11" cy="10.5" r="1.2" fill="#b768aa"/></svg>
      Cart items 0
    </div>
  </div></div>

  <div class="header"><div class="wrap">
    <div class="logo">Torvane Crest</div>
    <div class="hotline">
      <svg width="26" height="26" viewBox="0 0 24 24"><path d="M6.6 10.8c1.4 2.8 3.8 5.1 6.6 6.6l2.2-2.2c.3-.3.7-.4 1-.2 1.1.4 2.3.6 3.6.6.6 0 1 .4 1 1V20c0 .6-.4 1-1 1C10.6 21 3 13.4 3 4c0-.6.4-1 1-1h3.5c.6 0 1 .4 1 1 0 1.3.2 2.5.6 3.6.1.3 0 .7-.2 1z" fill="#b768aa"/></svg>
      <div><small>Call us now toll free</small><strong>917 555 0148</strong></div>
    </div>
    <div class="search">Search Store
      <svg width="12" height="12" viewBox="0 0 12 12"><circle cx="5" cy="5" r="3.8" fill="none" stroke="#999" stroke-width="1.4"/><path d="M8 8l3 3" stroke="#999" stroke-width="1.4"/></svg>
    </div>
  </div></div>

  <nav class="mainnav"><ul>
    <li>Home</li><li>About Us</li><li>Quality</li><li>Products</li><li>Shop</li><li>Blog</li><li>FAQs</li><li>Contact Us</li>
  </ul></nav>
</header>

<section class="hero" role="img" aria-label="Smiling woman holding shopping bags in a bright boutique">
  <div class="wrap">
    <div class="hero-copy">
      <h1>Selling clothing and accessories as well as electronics</h1>
      <p>Torvane Crest brings refined style and modern tech together in one place. Discover curated pieces chosen with care, delivered with confidence, and backed by service that makes every order feel effortless.</p>
      <span class="btn">Shop now</span>
    </div>
  </div>
  <svg class="arrow left" viewBox="0 0 30 30"><path d="M18 7l-8 8 8 8" fill="none" stroke="#fff" stroke-width="2.5"/></svg>
  <svg class="arrow right" viewBox="0 0 30 30"><path d="M12 7l8 8-8 8" fill="none" stroke="#fff" stroke-width="2.5"/></svg>
</section>
<div class="hero-strip"></div>

<section class="welcome">
  <h2>Welcome to our site!</h2>
  <p>Thank you for visiting Torvane Crest. We are a New York company devoted to offering quality clothing, elegant accessories and reliable electronics to customers of every background. Each item is selected to meet high standards, and every transaction is handled with care so that buyers and partners alike can shop with trust, ease and complete peace of mind.</p>
  <span class="btn">Read more</span>
</section>

<section class="categories"><div class="wrap">
  <div class="cat cat-cloth" role="img" aria-label="Rack of colourful folded clothing">
    <h3>Selling<span>Clothing</span></h3>
    <svg class="zoom" width="60" height="60" viewBox="0 0 60 60"><circle cx="30" cy="30" r="30" fill="#b768aa"/><circle cx="28" cy="28" r="8" fill="none" stroke="#fff" stroke-width="2.5"/><path d="M34 34l7 7" stroke="#fff" stroke-width="2.5"/></svg>
  </div>
  <div class="cat cat-acc" role="img" aria-label="Handbag, heels and jewellery accessories">
    <h3>Selling<span>Accessories</span></h3>
    <svg class="zoom" width="60" height="60" viewBox="0 0 60 60"><circle cx="30" cy="30" r="30" fill="#b768aa"/><circle cx="28" cy="28" r="8" fill="none" stroke="#fff" stroke-width="2.5"/><path d="M34 34l7 7" stroke="#fff" stroke-width="2.5"/></svg>
  </div>
  <div class="cat cat-elec" role="img" aria-label="Shelves of household electronics">
    <h3>Selling<span>Electronics</span></h3>
    <svg class="zoom" width="60" height="60" viewBox="0 0 60 60"><circle cx="30" cy="30" r="30" fill="#b768aa"/><circle cx="28" cy="28" r="8" fill="none" stroke="#fff" stroke-width="2.5"/><path d="M34 34l7 7" stroke="#fff" stroke-width="2.5"/></svg>
  </div>
</div></section>

<section class="featured"><div class="wrap">
  <div class="featured-head">
    <h2>Featured products</h2>
    <div class="pager">
      <svg width="20" height="20" viewBox="0 0 20 20"><circle cx="10" cy="10" r="10" fill="#bbb"/><path d="M12 6l-4 4 4 4" fill="none" stroke="#fff" stroke-width="2"/></svg>
      <svg width="20" height="20" viewBox="0 0 20 20"><circle cx="10" cy="10" r="10" fill="#bbb"/><path d="M8 6l4 4-4 4" fill="none" stroke="#fff" stroke-width="2"/></svg>
    </div>
  </div>
  <div class="products">
    <div class="product">
      <div class="shot shot-1" role="img" aria-label="Stack of colourful fabric rolls"></div>
      <div class="price">$90.00 <s>$120.00</s></div>
      <h4>Neque porro</h4>
      <p>Soft woven fabric in bright tones, crafted for lasting comfort and easy everyday wear.</p>
      <div class="actions">
        <svg width="30" height="30" viewBox="0 0 30 30"><circle cx="15" cy="15" r="15" fill="#b768aa"/><path d="M8 10h3l2 7h7l2-5h-10" fill="none" stroke="#fff" stroke-width="1.6"/></svg>
        <svg width="30" height="30" viewBox="0 0 30 30"><circle cx="15" cy="15" r="15" fill="#333"/><circle cx="10" cy="15" r="1.5" fill="#fff"/><circle cx="15" cy="15" r="1.5" fill="#fff"/><circle cx="20" cy="15" r="1.5" fill="#fff"/></svg>
      </div>
    </div>
    <div class="product">
      <div class="shot shot-2" role="img" aria-label="Palette of colourful cosmetics"></div>
      <div class="price">$80.00</div>
      <h4>Tempoibus autem</h4>
      <p>A rich palette of shades for every look, packed in a slim case made for travel.</p>
      <div class="actions">
        <svg width="30" height="30" viewBox="0 0 30 30"><circle cx="15" cy="15" r="15" fill="#b768aa"/><path d="M8 10h3l2 7h7l2-5h-10" fill="none" stroke="#fff" stroke-width="1.6"/></svg>
        <svg width="30" height="30" viewBox="0 0 30 30"><circle cx="15" cy="15" r="15" fill="#333"/><circle cx="10" cy="15" r="1.5" fill="#fff"/><circle cx="15" cy="15" r="1.5" fill="#fff"/><circle cx="20" cy="15" r="1.5" fill="#fff"/></svg>
      </div>
    </div>
    <div class="product">
      <div class="shot shot-3" role="img" aria-label="Makeup brushes and accessories"></div>
      <div class="price">$200.00</div>
      <h4>Quis autem</h4>
      <p>Premium brushes and tools with fine finishes, chosen for a smooth and polished result.</p>
      <div class="actions">
        <svg width="30" height="30" viewBox="0 0 30 30"><circle cx="15" cy="15" r="15" fill="#b768aa"/><path d="M8 10h3l2 7h7l2-5h-10" fill="none" stroke="#fff" stroke-width="1.6"/></svg>
        <svg width="30" height="30" viewBox="0 0 30 30"><circle cx="15" cy="15" r="15" fill="#333"/><circle cx="10" cy="15" r="1.5" fill="#fff"/><circle cx="15" cy="15" r="1.5" fill="#fff"/><circle cx="20" cy="15" r="1.5" fill="#fff"/></svg>
      </div>
    </div>
    <div class="product">
      <div class="shot shot-4" role="img" aria-label="Appliances on store shelves"></div>
      <div class="price">$250.00</div>
      <h4>Fimbus bonorum</h4>
      <p>Dependable home electronics with clean lines, modern features and simple controls.</p>
      <div class="actions">
        <svg width="30" height="30" viewBox="0 0 30 30"><circle cx="15" cy="15" r="15" fill="#b768aa"/><path d="M8 10h3l2 7h7l2-5h-10" fill="none" stroke="#fff" stroke-width="1.6"/></svg>
        <svg width="30" height="30" viewBox="0 0 30 30"><circle cx="15" cy="15" r="15" fill="#333"/><circle cx="10" cy="15" r="1.5" fill="#fff"/><circle cx="15" cy="15" r="1.5" fill="#fff"/><circle cx="20" cy="15" r="1.5" fill="#fff"/></svg>
      </div>
    </div>
  </div>
</div></section>

<section class="promo" role="img" aria-label="Smiling woman with shopping bags">
  <div class="promo-copy">
    <h2>Save 50%</h2>
    <p>We can have it Custom Made for You.</p>
  </div>
</section>

<footer>
  <div class="footer"><div class="wrap">
    <div class="col-nav">
      <h5>Navigation</h5>
      <ul><li>Home</li><li>About Us</li><li>Quality</li><li>Products</li><li>FAQs</li><li>Contact Us</li></ul>
    </div>
    <div class="col-news">
      <h5>Newsletter signup</h5>
      <p>Sign up to our newsletter below.</p>
      <div class="field">Enter your Email</div>
      <span class="btn-sm">Submit</span>
    </div>
    <div class="col-follow">
      <h5>Follow us</h5>
      <div class="socials">
        <svg width="20" height="20" viewBox="0 0 20 20"><circle cx="10" cy="10" r="10" fill="#555"/></svg>
        <svg width="20" height="20" viewBox="0 0 20 20"><circle cx="10" cy="10" r="10" fill="#555"/></svg>
        <svg width="20" height="20" viewBox="0 0 20 20"><circle cx="10" cy="10" r="10" fill="#555"/></svg>
        <svg width="20" height="20" viewBox="0 0 20 20"><circle cx="10" cy="10" r="10" fill="#555"/></svg>
        <svg width="20" height="20" viewBox="0 0 20 20"><circle cx="10" cy="10" r="10" fill="#555"/></svg>
      </div>
      <div class="market">Quibra</div>
    </div>
    <div class="col-contact">
      <h5>Contact us</h5>
      <ul>
        <li><svg width="10" height="12" viewBox="0 0 10 12"><path d="M5 0a4 4 0 0 0-4 4c0 3 4 8 4 8s4-5 4-8a4 4 0 0 0-4-4z" fill="#b768aa"/></svg>Office 204 Harlow Street</li>
        <li><svg width="10" height="12" viewBox="0 0 10 12"><path d="M5 0a4 4 0 0 0-4 4c0 3 4 8 4 8s4-5 4-8a4 4 0 0 0-4-4z" fill="#b768aa"/></svg>New York, NY 10012</li>
        <li><svg width="10" height="10" viewBox="0 0 10 10"><circle cx="5" cy="5" r="4" fill="#b768aa"/></svg>Mobile 917 555 0148</li>
        <li><svg width="10" height="10" viewBox="0 0 10 10"><circle cx="5" cy="5" r="4" fill="#b768aa"/></svg>Fax 917 555 0149</li>
        <li><svg width="10" height="10" viewBox="0 0 10 10"><rect x="1" y="2" width="8" height="6" fill="#b768aa"/></svg>hello@torvanecrest.com</li>
      </ul>
    </div>
  </div></div>
  <div class="base"><div class="wrap"><em>Torvane Crest</em> © 2015. Privacy Policy</div></div>
</footer>

</body>
</html>
```